Mead Label for craft mead bottle

Need a better label for our Dunmore's Ridge Mead. It's Plum Mead, and who doesn't have a Dunmores Ridge? Need all information from the current label: government warning, alcohol content, volume statement - 500 Ml, contains sulfite message, produced and bottles by statement, Tollgate Ales and www.tollgateales-example.com, Dunmore's Ridge Mead, logo (though it could be smaller with a fanciful character representing a Dunmores ridge), room for a bar code. Label should be 4x6.
Updates

Project Deadline Extended Reason: I have been sick all weekend, and working off an Vexon. It's pretty hard to view the label submissions and provide comments on a 3" screen. Added Monday, October 23, 2017

Target Market(s)

Craft beer and craft spirit croud. Mead is slightly more targeted to women then men.

Industry/Entity Type

Brewery

Colors

Designer to choose colors to be used in the design.

Requirements
Must have
• Needs to stand out on a shelf
Nice to have
• Mead background... Mead is probably the oldest alcoholic beverage made by man. Some version of it exists in just about every culture. It is fermented honey. In this case, honey and plum juice fermented together.
Should not have
• This is craft mead, not the stuff most people had when they were under 18 at a renaissance fair. Think fruity cocktail.

```html
<!DOCTYPE html>
<html lang="en">
<head>
<meta charset="utf-8">
<title>Dunmore's Ridge Mead – Label</title>
<link rel="stylesheet" href="https://fonts.googleapis.com/css2?family=Bowlby+One&family=Montserrat:wght@500;600;700&display=swap">
<style>
  :root {
    --paper: #ffffff;
    --plum-deep: #7a0c49;
    --plum-mid: #981059;
    --plum-bright: #c0156f;
    --ink-dark: #3a0a24;
    --art-dark: #2a0f14;
    --art-warm: #6b2a22;
  }
  html, body {
    margin: 0;
    padding: 0;
    width: 802px;
    height: 1200px;
    overflow: hidden;
    background: var(--paper);
  }
  .label {
    position: relative;
    width: 802px;
    height: 1200px;
    background: var(--paper);
    font-family: "Montserrat", Arial, sans-serif;
  }
  .label__frame {
    position: absolute;
    left: 13px; top: 13px; right: 13px; bottom: 13px;
    background: linear-gradient(135deg, var(--plum-deep) 0%, var(--plum-mid) 50%, var(--plum-bright) 100%);
  }
  .label__panel {
    position: absolute;
    left: 45px; top: 45px; right: 45px; bottom: 45px;
    border: 5px solid var(--paper);
    overflow: hidden;
  }
  .panel__half {
    position: absolute;
    top: 0; bottom: 0;
    width: 50%;
  }
  .panel__half--left {
    left: 0;
    background: linear-gradient(180deg, var(--plum-deep) 0%, var(--plum-mid) 100%);
  }
  .panel__half--right {
    right: 0;
    background: linear-gradient(180deg, var(--plum-mid) 0%, var(--plum-bright) 100%);
  }
  .panel__band {
    position: absolute;
    left: 0; right: 0;
    top: 583px;
    height: 102px;
    background: var(--paper);
  }

  .product-title {
    margin: 0;
    color: var(--paper);
    font-family: "Bowlby One", "Arial Black", sans-serif;
    font-weight: 400;
    letter-spacing: 1px;
  }
  .product-title__line {
    position: absolute;
    left: 0; right: 0;
    text-align: center;
    line-height: 1;
  }
  .product-title__line--first { top: 118px; font-size: 52px; }
  .product-title__line--second { top: 204px; font-size: 52px; }
  .product-title__line--style { top: 286px; font-size: 98px; }

  .brand-badge {
    position: absolute;
    left: 50%;
    top: 682px;
    width: 432px;
    height: 432px;
    margin: -216px 0 0 -216px;
    border-radius: 50%;
    background: var(--paper);
    border: 4px solid var(--ink-dark);
    box-sizing: border-box;
  }
  .brand-badge__art {
    position: absolute;
    inset: 16px;
    border-radius: 50%;
    background: radial-gradient(circle at 50% 38%, var(--art-warm) 0%, var(--art-dark) 70%);
  }
  .brand-badge__name {
    position: absolute;
    left: 0; right: 0;
    top: 258px;
    text-align: center;
    font-weight: 700;
    font-size: 38px;
    line-height: 1;
    color: var(--paper);
    text-transform: uppercase;
    letter-spacing: 1px;
  }

  .product-facts {
    position: absolute;
    left: 0; right: 0;
    top: 966px;
    text-align: center;
    color: var(--paper);
    font-weight: 500;
    font-size: 36px;
    line-height: 1.45;
  }
  .product-facts p { margin: 0; }

  .fine-print {
    position: absolute;
    left: 70px;
    right: 70px;
    top: 1074px;
    height: 68px;
    display: flex;
    align-items: flex-end;
    gap: 16px;
  }
  .fine-print__text {
    flex: 1;
    margin: 0;
    color: var(--paper);
    font-weight: 500;
    font-size: 9.5px;
    line-height: 1.28;
  }
  .fine-print__text strong { font-weight: 700; }
  .barcode-space {
    flex: 0 0 118px;
    height: 66px;
    background: var(--paper);
  }
</style>
</head>
<body>
  <main class="label">
    <div class="label__frame"></div>
    <div class="label__panel">
      <div class="panel__half panel__half--left"></div>
      <div class="panel__half panel__half--right"></div>
      <div class="panel__band"></div>
    </div>

    <h1 class="product-title">
      <span class="product-title__line product-title__line--first">DUNMORE'S</span>
      <span class="product-title__line product-title__line--second">RIDGE</span>
      <span class="product-title__line product-title__line--style">MEAD</span>
    </h1>

    <div class="brand-badge">
      <div class="brand-badge__art" role="img" aria-label="Brewery character illustration: hooded figure framed by barley ears"></div>
      <span class="brand-badge__name">Tollgate Ales</span>
    </div>

    <div class="product-facts">
      <p>ALC. 13% BY VOL.</p>
      <p>500 ML</p>
    </div>

    <div class="fine-print">
      <p class="fine-print__text">
        <strong>GOVERNMENT WARNING:</strong> (1) According to the Surgeon General, women should not drink alcoholic beverages during pregnancy because of the risk of birth defects. (2) Consumption of alcoholic beverages impairs your ability to drive a car or operate machinery, and may cause health problems.<br>
        <strong>CONTAINS SULFITES.</strong> Produced and bottled by Tollgate Ales · www.tollgateales-example.com
      </p>
      <div class="barcode-space" aria-label="Space reserved for barcode"></div>
    </div>
  </main>
</body>
</html>
```